Letterhead and matching envelope design for a dental office

We need a new stationary design, letterhead and envelope #10, for a dental office in Denver area. We are called Brightfield Dental. We want a simple and minimalistic design but not a boring design. I wish to have one good point that makes it look professional. I have attached our logo. Feel free to use either one. I want the design for letterhead and envelope look like a "matching pair" but not look the same. The envelope doesn't have to be white and it will have an address window on bottom left.

Target Market(s)

everyone who visits dentist (adults)

Industry/Entity Type

Dental

Font styles to use
Other font styles liked:
• close to font on logo or something that matches well

Requirements
Must have
• professional
• simple, minimalistic
• unique point that stands out
Nice to have
• matching but not same design for letterhead and envelope
Should not have
• not look like all the other boring designs
• no flowery, distracting feats

```html
<!DOCTYPE html>
<html lang="en">
<head>
<meta charset="utf-8">
<title>Brightfield Dental – Letterhead and Envelope</title>
<link href="https://fonts.googleapis.com/css2?family=Lato:ital,wght@0,400;0,700;1,400&display=swap" rel="stylesheet">
<style>
  :root {
    --green: #43b649;
    --green-faint: rgba(67, 182, 73, 0.10);
    --paper: #ebebeb;
    --backdrop: #d9d9d9;
    --ink: #2f2f2f;
    --ink-soft: #4a4a4a;
    --rule: #9a9a9a;
    --white: #ffffff;
  }
  * { box-sizing: border-box; margin: 0; padding: 0; }
  html, body {
    width: 1200px; height: 809px; overflow: hidden;
    background: var(--backdrop);
    font-family: "Lato", Arial, sans-serif;
    color: var(--ink);
  }
  .canvas { position: relative; width: 1200px; height: 809px; }

  /* Letterhead */
  .letterhead {
    position: absolute; left: 54px; top: 54px;
    width: 496px; height: 699px;
    background: var(--paper);
    box-shadow: 0 1px 3px rgba(0,0,0,0.25);
    overflow: hidden;
  }
  .motif {
    position: absolute;
    background: radial-gradient(ellipse at center, var(--green-faint) 0%, var(--green-faint) 55%, rgba(67,182,73,0) 75%);
  }
  .letterhead .motif { left: 40px; top: 340px; width: 460px; height: 380px; }
  .brand-name {
    position: absolute;
    font-family: "Lato", Arial, sans-serif;
    font-weight: 700;
    color: var(--green);
    letter-spacing: 1.2px;
    text-transform: uppercase;
    white-space: nowrap;
  }
  .letterhead .brand-name { left: 43px; top: 94px; font-size: 11px; }
  .brand-place {
    position: absolute;
    font-size: 5.5px; letter-spacing: 5px; color: var(--green);
  }
  .letterhead .brand-place { left: 60px; top: 109px; }
  .sender-address {
    position: absolute; font-size: 8.8px; line-height: 13.6px; color: var(--ink-soft);
  }
  .letterhead .sender-address { left: 352px; top: 80px; }
  .salutation { position: absolute; left: 36px; top: 219px; font-size: 8.8px; }
  .letter-body {
    position: absolute; left: 36px; top: 250px; width: 440px;
    font-size: 8.6px; line-height: 10.9px; text-align: justify;
  }
  .letter-body p { margin-bottom: 10.9px; }
  .sign-off { position: absolute; left: 36px; top: 457px; font-size: 8.8px; line-height: 12.4px; }
  .signature {
    position: absolute; left: 112px; top: 468px; width: 76px; height: 30px;
    background: rgba(40, 80, 170, 0.10); border-radius: 3px;
  }
  .contact-bar {
    position: absolute; left: 38px; top: 648px; width: 440px; height: 32px;
    display: flex; align-items: center; font-size: 8.6px; color: var(--ink-soft);
  }
  .contact-group { display: flex; flex-direction: column; gap: 3px; }
  .contact-line { display: flex; align-items: center; gap: 5px; white-space: nowrap; }
  .contact-line svg { width: 9px; height: 9px; fill: var(--green); }
  .divider { width: 1px; height: 30px; background: var(--rule); margin: 0 28px 0 40px; }
  .web { color: var(--green); font-style: italic; }

  /* Envelope */
  .envelope { position: absolute; left: 568px; top: 394px; width: 584px; height: 360px; }
  .envelope-body {
    position: absolute; left: 0; top: 98px; width: 584px; height: 262px;
    background: var(--paper);
    box-shadow: 0 1px 3px rgba(0,0,0,0.25);
    overflow: hidden;
  }
  .envelope-flap { position: absolute; left: 0; top: 0; width: 584px; height: 99px; }
  .envelope .motif { left: 260px; top: 40px; width: 330px; height: 240px; }
  .envelope .brand-name { left: 31px; top: 52px; font-size: 10.5px; }
  .envelope .brand-place { left: 49px; top: 66px; font-size: 5px; }
  .envelope .sender-address { left: 31px; top: 214px; }
  .seal {
    position: absolute; left: 254px; top: 16px; width: 80px; height: 60px;
    display: flex; flex-direction: column; align-items: center; gap: 4px;
  }
  .seal-dot { width: 14px; height: 14px; border: 1.5px solid var(--white); border-radius: 50%; }
  .seal-name {
    color: var(--white); font-weight: 700; font-size: 6.5px;
    letter-spacing: 1.5px; text-transform: uppercase; text-align: center; line-height: 9px;
  }
</style>
</head>
<body>
<main class="canvas">

  <section class="letterhead" aria-label="Letterhead">
    <div class="motif" role="img" aria-label="Large faint leaf motif in the background"></div>

    <div class="brand-name">Brightfield Dental</div>
    <div class="brand-place">Lakewood</div>

    <address class="sender-address" style="font-style:normal">
      2140 Aspen Ridge Drive<br>Lakewood, Colorado 80226
    </address>

    <p class="salutation">Dear Mr. Smith,</p>

    <div class="letter-body">
      <p>Lorem ipsum dolor sit amet, consectetur adipiscing elit. Donec orci purus, luctus vitae dignissim eu, iaculis sed purus. Vivamus faucibus, ipsum nec aliquet viverra, leo mauris condimentum ligula, sit amet sagittis enim ligula quis arcu. Nam egestas tortor id nisi porttitor mattis. In tortor ante, ultricies in suscipit a, tempus non massa. Vivamus et auctor mi.</p>
      <p>Fusce vel massa nulla. Phasellus nec eros mauris, et scelerisque orci. Donec malesuada orci vitae nulla accumsan porta a id massa. Quisque accumsan iaculis magna sit amet fringilla. Maecenas consequat, magna eget tincidunt semper, odio nibh rutrum mi, id feugiat ante nisi eu risus. Vestibulum nunc orci, rhoncus a placerat in, ultricies in mi. Cras mattis varius eros, vel fringilla nisi suscipit eget.</p>
      <p>Quisque scelerisque sagittis nulla at porttitor. Mauris a justo et tellus interdum tristique. Sed id augue vitae urna euismod commodo aliquet a quam. Pellentesque arcu velit, cursus et malesuada ut, consequat et diam. Nullam erat sem, rhoncus id ullamcorper vitae, rhoncus et arcu. In ultricies ultricies nulla, ut rutrum nisi iaculis at. Donec eu magna a metus ornare faucibus.</p>
      <p>Fusce aliquet faucibus ultricies. Morbi semper, est id tincidunt gravida, sem arcu adipiscing lacus, ac bibendum nulla leo eu purus. Quisque nec diam sed risus consectetur a ccumsan quis quis nibh. Vestibulum id purus lorem.</p>
    </div>

    <div class="sign-off">Mara Ellison<br>Co-Founder &amp; CEO</div>
    <div class="signature" role="img" aria-label="Handwritten signature"></div>

    <div class="contact-bar">
      <div class="contact-group">
        <span class="contact-line">
          <svg viewBox="0 0 10 10" aria-hidden="true"><path d="M2 0.5 L3.6 2.8 L2.7 3.8 C3.3 5.1 4.6 6.5 6 7.2 L7 6.3 L9.5 7.8 L8.6 9.5 C4.5 9.3 0.8 5.6 0.5 1.4 Z"/></svg>
          303 555 0148
        </span>
        <span class="contact-line">
          <svg viewBox="0 0 10 10" aria-hidden="true"><path d="M2.5 0 H7.5 A1 1 0 0 1 8.5 1 V9 A1 1 0 0 1 7.5 10 H2.5 A1 1 0 0 1 1.5 9 V1 A1 1 0 0 1 2.5 0 Z M2.8 1.3 V7.8 H7.2 V1.3 Z"/></svg>
          303 555 0172
        </span>
      </div>
      <div class="divider"></div>
      <div class="contact-group">
        <span class="contact-line">
          <svg viewBox="0 0 10 10" aria-hidden="true"><path d="M2.5 0.5 H7.5 V3 H2.5 Z M0.5 3.5 H9.5 V8 H8 V6.5 H2 V8 H0.5 Z M2.5 7 H7.5 V9.5 H2.5 Z"/></svg>
          303 555 0190
        </span>
        <span class="contact-line">
          <svg viewBox="0 0 10 10" aria-hidden="true"><path d="M0.5 2 H9.5 V8.5 H0.5 Z M1 2.4 L5 5.6 L9 2.4" stroke="#ebebeb" stroke-width="0.8"/></svg>
          hello@brightfielddental.com
        </span>
      </div>
      <div class="divider"></div>
      <span class="web">www.brightfielddental.com</span>
    </div>
  </section>

  <section class="envelope" aria-label="Envelope">
    <svg class="envelope-flap" viewBox="0 0 584 99" aria-hidden="true">
      <path d="M0 99 L10 45 Q18 0 64 0 L522 0 Q566 0 574 45 L584 99 Z" fill="var(--green)"/>
    </svg>
    <div class="seal">
      <div class="seal-dot"></div>
      <div class="seal-name">Brightfield<br>Dental</div>
    </div>
    <div class="envelope-body">
      <div class="motif" role="img" aria-label="Faint leaf motif in the background"></div>
      <div class="brand-name">Brightfield Dental</div>
      <div class="brand-place">Lakewood</div>
      <address class="sender-address" style="font-style:normal">
        2140 Aspen Ridge Drive<br>Lakewood, Colorado 80226
      </address>
    </div>
  </section>

</main>
</body>
</html>
```